HVAC company business card design

We need a business card design for a HVAC company. The design must look professional. Both sides will be used. The total data to be on the business card is
Name
Position
Email
Direct Phone/Moile Phone
Company Contacts /Address, Phone, Fax, web)
All data will be submit once the design is confirmed. For generic purposes use;
Emre Toksoy
Managing Director
+902324815263 (Mobile)
4712 Sokak No: 9 KBSE Yenikent IZMIR TURKEY
Tel: +902324815263 Fax : +902324815269
www.luvon.com.tr

Target Market(s)

HVAC

Industry/Entity Type

Business

Contact Information for Business Card

The total data to be on the business card is
Name
Position
Email
Direct Phone/Moile Phone
Emre Toksoy
Managing Director
+902324815263 (Mobile)
www.luvon.com.tr
The BC will use both sides of the card. The front will include the full logo and the details for the business card holder. The business card can be divided into vertical/horizontal or to a special shape. The common data like the company address/phone/fax should be indicated elsewehere. The back can contain some part or the whole logo and must contain the web address.

Font styles to use
Serif
Sans Serif

Colors
0355a3
cfdfed

Requirements
Should not have
• Please be careful with the fonts, it shouldnt be too small or too big and must not interfere with the logo fonts. If you need to use a curvy shape please do not use as the logo is already curvy or use the curves from the logo (if it looks good, otherwise forget it)
• We are not in favor of pictograms, only if they are perfect use them.

```html
<!DOCTYPE html>
<html lang="en">
<head>
<meta charset="utf-8">
<title>Luvon business card</title>
<link rel="stylesheet" href="https://fonts.googleapis.com/css2?family=Source+Sans+3:wght@400;600&family=Michroma&display=swap">
<style>
  :root {
    --bg: #dcdcdc;
    --card: #ffffff;
    --card-shade: #f4f4f5;
    --navy: #3a3f5c;
    --blue: #0355a3;
    --blue-light: #cfdfed;
    --text: #3f4358;
    --muted: #6b6f80;
    --faint: #ececee;
    --rule: #e3e3e6;
  }
  * { box-sizing: border-box; margin: 0; padding: 0; }
  html, body { width: 1200px; height: 1200px; overflow: hidden; }
  body {
    background: var(--bg);
    font-family: "Source Sans 3", Arial, sans-serif;
    position: relative;
  }
  .card {
    position: absolute;
    left: 220px;
    width: 760px;
    height: 430px;
    border-radius: 28px;
    background: linear-gradient(160deg, var(--card) 40%, var(--card-shade));
    box-shadow: 0 6px 18px rgba(0,0,0,0.18);
    overflow: hidden;
  }
  .card--front { top: 150px; }
  .card--back { top: 620px; }

  .deco-circle {
    position: absolute;
    width: 380px; height: 380px;
    border-radius: 50%;
    background: var(--faint);
    right: -60px; top: -60px;
  }

  .brand {
    position: absolute;
    display: flex;
    align-items: center;
    gap: 22px;
  }
  .brand__dot {
    width: 74px; height: 74px;
    border-radius: 50%;
    background: var(--blue);
  }
  .brand__name {
    font-weight: 600;
    font-size: 78px;
    letter-spacing: 6px;
    color: var(--navy);
    line-height: 1;
  }
  .card--front .brand { left: 150px; top: 172px; }
  .card--back .brand { left: 80px; top: 178px; }
  .card--back .brand__dot { width: 54px; height: 54px; }
  .card--back .brand__name { font-size: 58px; letter-spacing: 4px; }

  .divider {
    position: absolute;
    left: 420px; top: 40px;
    width: 1px; height: 300px;
    background: var(--rule);
  }

  .holder {
    position: absolute;
    left: 462px; top: 72px;
    color: var(--text);
  }
  .holder__name {
    font-family: "Michroma", Arial, sans-serif;
    font-size: 24px;
    color: var(--navy);
    letter-spacing: 1px;
    text-transform: uppercase;
  }
  .holder__role {
    font-size: 15px;
    color: var(--muted);
    margin-top: 2px;
  }
  .contacts { list-style: none; margin-top: 20px; }
  .contacts li {
    display: flex; align-items: center; gap: 10px;
    font-size: 17px; line-height: 26px;
  }
  .contacts svg { width: 16px; height: 16px; fill: var(--blue); flex: none; }
  .address { margin-top: 12px; font-size: 17px; line-height: 24px; }

  .band-navy {
    position: absolute;
    left: 0; bottom: 0;
    width: 100%; height: 16px;
    background: var(--navy);
  }
  .band-web {
    position: absolute;
    right: 0; bottom: 0;
    width: 390px; height: 80px;
    background: linear-gradient(90deg, var(--blue), #1a74c4);
    clip-path: polygon(14px 0, 100% 0, 100% 100%, 0 100%);
    display: flex; align-items: center; justify-content: center;
  }
  .band-web span {
    color: #fff;
    font-size: 19px;
    letter-spacing: 1px;
  }
</style>
</head>
<body>
  <section class="card card--front" aria-label="Card front">
    <div class="deco-circle"></div>
    <div class="brand">
      <div class="brand__dot"></div>
      <div class="brand__name">LUVON</div>
    </div>
  </section>

  <section class="card card--back" aria-label="Card back">
    <div class="deco-circle"></div>
    <div class="brand">
      <div class="brand__dot"></div>
      <div class="brand__name">LUVON</div>
    </div>
    <div class="divider"></div>
    <div class="holder">
      <div class="holder__name">Emre Toksoy</div>
      <div class="holder__role">Managing Director</div>
      <ul class="contacts">
        <li><svg viewBox="0 0 16 16" aria-hidden="true"><path d="M4 1h8a1 1 0 0 1 1 1v12a1 1 0 0 1-1 1H4a1 1 0 0 1-1-1V2a1 1 0 0 1 1-1zm1 2v9h6V3zm3 10.2a.8.8 0 1 0 0 .01z"/></svg>+902324815263</li>
        <li><svg viewBox="0 0 16 16" aria-hidden="true"><path d="M2 6c0-2 3-3 6-3s6 1 6 3v1h-3V5.5H5V7H2zm2 2h8l1 6H3zm4 1.5a2 2 0 1 0 0 4 2 2 0 0 0 0-4z"/></svg>+902324815264</li>
        <li><svg viewBox="0 0 16 16" aria-hidden="true"><path d="M4 1h6l2 2v3H4zm-2 6h12a1 1 0 0 1 1 1v6H1V8a1 1 0 0 1 1-1zm2 3v1h2v-1zm4 0v1h4v-1z"/></svg>+902324815269</li>
      </ul>
      <div class="address">4712 Sokak No: 9 KBSE<br>Yenikent IZMIR TURKEY</div>
    </div>
    <div class="band-navy"></div>
    <div class="band-web"><span>www.luvon.com.tr</span></div>
  </section>
</body>
</html>
```